Talvin Foundation Letterhead

We are a newly established non profit registered in Maryland but operates in Africa, south of the sahara. We offer scholarships to deserving young adults from high school through college. Our color theme for our existing logo is purple, we want a design that is stylish, spellbinding yet a letterhead that projects seriousness. More information on www.thetalvinfoundation.example

Target Market(s)

High school and college students in sub saharan African as well as our donors in the US

Industry/Entity Type

Non Profit

Font styles to use
Script

Requirements
Must have
• Logo at the top and if possible watermark the logo in the middle of the letterhead, contact address,
Should not have
• NA

```html
<!DOCTYPE html>
<html lang="en">
<head>
<meta charset="utf-8">
<title>Talvin Foundation Letterhead</title>
<link rel="stylesheet" href="https://fonts.googleapis.com/css2?family=Roboto:wght@400;500;700&family=Kaushan+Script&display=swap">
<style>
  :root {
    --bg: #e4e4e6;
    --paper: #ffffff;
    --ink: #1b1b1b;
    --purple: #9a62b0;
    --purple-deep: #7d4a9a;
    --lavender: #cfcde0;
    --muted: #555555;
  }
  * { box-sizing: border-box; margin: 0; padding: 0; }
  html, body { width: 1200px; height: 949px; overflow: hidden; background: var(--bg); }
  .canvas { position: relative; width: 1200px; height: 949px; }
  .letterhead {
    position: absolute; left: 282px; top: 24px;
    width: 636px; height: 900px;
    background: var(--paper);
    box-shadow: 0 8px 24px rgba(0,0,0,0.12);
    overflow: hidden;
    font-family: "Roboto", Arial, sans-serif;
    color: var(--ink);
  }
  .brand { position: absolute; left: 56px; top: 58px; display: flex; align-items: center; gap: 12px; }
  .brand-dot { width: 34px; height: 34px; border-radius: 50%; background: var(--purple); }
  .brand-name { font-size: 19px; font-weight: 500; color: var(--purple-deep); letter-spacing: 1.5px; text-transform: uppercase; }
  .contact {
    position: absolute; right: 56px; top: 52px;
    border-left: 1px solid var(--purple); padding-left: 10px;
    font-size: 8.5px; line-height: 1.35;
  }
  .contact-label { color: var(--purple); text-transform: uppercase; letter-spacing: 0.5px; }
  .contact-value { color: var(--muted); margin-bottom: 4px; }
  .recipient { position: absolute; left: 56px; top: 170px; font-size: 9.5px; line-height: 1.35; }
  .recipient-name { font-weight: 700; font-size: 11px; }
  .body-copy { position: absolute; left: 56px; top: 232px; width: 524px; font-size: 9.6px; line-height: 1.5; }
  .body-copy p + p { margin-top: 16px; }
  .closing { position: absolute; left: 56px; top: 452px; font-size: 9.6px; }
  .signature { position: absolute; left: 56px; top: 472px; font-family: "Kaushan Script", cursive; font-size: 36px; color: var(--ink); }
  .signer { position: absolute; left: 56px; top: 528px; font-size: 10px; font-weight: 500; line-height: 1.35; }
  .swoosh { position: absolute; left: 0; top: 0; width: 636px; height: 900px; }
</style>
</head>
<body>
<div class="canvas">
  <div class="letterhead">
    <svg class="swoosh" viewBox="0 0 636 900" aria-hidden="true">
      <path d="M0 900 C 180 860, 420 760, 636 470 L 636 484 C 440 760, 220 880, 40 900 Z" fill="var(--lavender)"/>
      <path d="M320 900 C 470 820, 590 640, 636 500 L 636 900 Z" fill="var(--purple)"/>
    </svg>

    <header class="brand">
      <span class="brand-dot"></span>
      <span class="brand-name">The Talvin Foundation Inc</span>
    </header>

    <div class="contact">
      <div class="contact-label">Email:</div>
      <div class="contact-value">admin@thetalvinfoundation.example</div>
      <div class="contact-label">Web:</div>
      <div class="contact-value">www.thetalvinfoundation.example</div>
    </div>

    <div class="recipient">
      <div class="recipient-name">JOHN SMITH</div>
      <div>Street Name,City Name.</div>
      <div>Zip Coad 0000</div>
    </div>

    <main class="body-copy">
      <p>Lorem Ipsum is simply dummy text of the printing and typesetting industry. Lorem Ipsum has been the industry's standard dummy text ever since the 1500s, when an unknown printer took a galley of type and scrambled it to make a type specimen book. It has survived not only five centuries,but also the leap into electronic typesetting, remaining essentially unchanged. It was popularised in the 1960s with the release of Veltrane sheets containing Lorem Ipsum passages, and more recently with desktop publishing software like Quillon PageSetter including versions of Lorem Ipsum.</p>
      <p>It is a long established fact that a reader will be distracted by the readable content of a page when looking at its layout. The point of using Lorem Ipsum is that it has a more-or-less normal distribution of letters, as opposed to using 'Content here, content here', making it look like readable English. Many desktop and publishing packages and web page editors now use Lorem Ipsum as their default model text, and a search for 'lorem ipsum' will uncover many web sites still in their infancy. Various versions have evolved over the years, sometimes by accident, sometimes on purpose (injected humour and the like).</p>
    </main>

    <div class="closing">Regards,</div>
    <div class="signature">John Doe</div>
    <div class="signer">
      <div>John Doe</div>
      <div>General Maneger</div>
    </div>
  </div>
</div>
</body>
</html>
```